Kettle Ledger Business Card design

We need a stand out business card design for Accounting practice based in Australia specialising in pubs, clubs and hotels. We help venues maximise margins, create time and manage cashflow. One club we have been working with for the last 6 months has increased revenue by 3% and margin by 5% in this time frame. We have a back office outsourced system that costs less than having a full time employee and also allows the venues the added benefit of:<br/>-using the office space to become a revenue generating opportunity. <br/>-a complete system to enhance governance, accountability and efficiency within their operation<br/>-52 weeks cover so no hassle to cover annual/sick .. leave<br/><br/>We would like to see designs that use the colours of our logo (green & blue).
Target Market(s)
Australian Pubs, Clubs & Hotels abookkeeping, accounting and tax services
Industry/Entity Type
Accountant
Contact Information for Business Card
Miriam Oakley CPA
Principal
Accountant Tax Agent
Miriam@KettleLedger-example.com.au
0418693142
www.kettleledger-example.com.au
Accounting / Payroll / Tax / SMSF / Technology
Colors
Designer to choose colors to be used in the design.
Look and feel
Each slider illustrates characteristics of the customer's brand and the style your logo design should communicate.

```html
<!DOCTYPE html>
<html lang="en">
<head>
<meta charset="utf-8">
<title>Kettle Ledger Business Card</title>
<link rel="stylesheet" href="https://fonts.googleapis.com/css2?family=Arimo:wght@400;700&display=swap">
<style>
  :root {
    --backdrop: #d3d3ce;
    --card: #fbfafc;
    --green: #13783f;
    --blue: #233e8f;
    --ink: #1d1d1d;
  }
  * { box-sizing: border-box; margin: 0; padding: 0; }
  html, body { width: 1200px; height: 801px; overflow: hidden; }
  body {
    background: var(--backdrop);
    font-family: "Arimo", Arial, sans-serif;
    position: relative;
  }
  .card {
    position: absolute;
    top: 236px;
    width: 540px;
    height: 330px;
    background: var(--card);
    border-bottom: 4px solid var(--green);
    box-shadow: 0 6px 18px rgba(0,0,0,0.18);
  }
  .card--front { left: 40px; }
  .card--back { left: 620px; }

  .brand {
    display: flex;
    align-items: center;
    gap: 12px;
    color: var(--blue);
    font-weight: 700;
    white-space: nowrap;
  }
  .brand__dot {
    border-radius: 50%;
    border: 3px solid var(--green);
    flex: none;
  }

  .card--front .brand {
    position: absolute;
    left: 34px;
    top: 104px;
    font-size: 25px;
  }
  .card--front .brand__dot { width: 34px; height: 34px; }

  .divider {
    position: absolute;
    left: 262px;
    top: 44px;
    width: 1px;
    height: 150px;
    background: var(--green);
  }

  .contact {
    position: absolute;
    left: 282px;
    top: 44px;
    color: var(--ink);
  }
  .contact__name {
    color: var(--green);
    font-weight: 700;
    font-size: 21px;
    margin-bottom: 4px;
  }
  .contact__role { font-size: 13px; line-height: 1.25; }
  .contact__list { list-style: none; margin-top: 18px; }
  .contact__item {
    display: flex;
    align-items: center;
    gap: 8px;
    font-size: 11.5px;
    line-height: 1.9;
    white-space: nowrap;
  }
  .contact__icon { width: 13px; height: 13px; flex: none; }

  .services {
    position: absolute;
    left: 34px;
    right: 34px;
    bottom: 36px;
    display: flex;
    justify-content: space-between;
    list-style: none;
    color: var(--green);
    font-size: 14px;
  }

  .card--back .brand {
    position: absolute;
    left: 0; right: 0;
    top: 132px;
    justify-content: center;
    font-size: 50px;
    gap: 20px;
  }
  .card--back .brand__dot { width: 66px; height: 66px; border-width: 5px; }
</style>
</head>
<body>
  <section class="card card--front">
    <div class="brand"><span class="brand__dot"></span>Kettle Ledger</div>
    <div class="divider"></div>
    <div class="contact">
      <p class="contact__name">Miriam Oakley CPA</p>
      <p class="contact__role">Principal</p>
      <p class="contact__role">Accountant Tax Agent</p>
      <ul class="contact__list">
        <li class="contact__item">
          <svg class="contact__icon" viewBox="0 0 16 16"><path d="M4 1l3 3-2 2c1 2 3 4 5 5l2-2 3 3-2 3C7 15 1 9 1 3z" fill="var(--green)"/></svg>
          0418693142
        </li>
        <li class="contact__item">
          <svg class="contact__icon" viewBox="0 0 16 16"><rect x="1" y="3" width="14" height="10" fill="none" stroke="var(--green)" stroke-width="1.4"/><path d="M1 3l7 6 7-6" fill="none" stroke="var(--green)" stroke-width="1.4"/></svg>
          Miriam@KettleLedger-example.com.au
        </li>
        <li class="contact__item">
          <svg class="contact__icon" viewBox="0 0 16 16"><circle cx="8" cy="8" r="6.5" fill="none" stroke="var(--green)" stroke-width="1.3"/><ellipse cx="8" cy="8" rx="3" ry="6.5" fill="none" stroke="var(--green)" stroke-width="1.1"/><path d="M1.5 8h13M2.5 5h11M2.5 11h11" stroke="var(--green)" stroke-width="1"/></svg>
          www.kettleledger-example.com.au
        </li>
      </ul>
    </div>
    <ul class="services">
      <li>Accounting</li>
      <li>Payroll</li>
      <li>Tax</li>
      <li>SMSF</li>
      <li>Technology</li>
    </ul>
  </section>

  <section class="card card--back">
    <div class="brand"><span class="brand__dot"></span>Kettle Ledger</div>
  </section>
</body>
</html>
```